Graphic Design job - Lantern Fair Social Media Graphics

Design Twitter/Instagram Cover Photo First. And other social media graphics to follow. Looking for a modern, fresh, fun take on design for this cultural event to attract a mainstream audience in a diverse and cool city (Toronto), as opposed to traditional design images which is what has been done before.

About the event: There will be a street food fair, acrobatics, music and dance performances coming from the Meridian Opera House, a local 18 member jazz band and 3 giant 30 feet dragons (very IG worthy). Interactive experiences like getting to try traditional Opera Makeup and headdress as well as being part of a Han Dynasty royal wedding. Something for everyone.

Target Market(s)

Downtown Crowd - 25-75. Families. Cultural and Performance Events Fans. Weekend festival goers. Street Food Fans. Millennials who like IG opportunities.

Requirements
Must have
• Copy:
• Toronto Lantern Fair
• Corwin Ashby Square
• July 15 & 16
• #LanternFairTo

```html
<!DOCTYPE html>
<html lang="en">
<head>
<meta charset="utf-8">
<title>Toronto Lantern Fair</title>
<link href="https://fonts.googleapis.com/css2?family=Montserrat:wght@400;500;800;900&display=swap" rel="stylesheet">
<style>
  :root {
    --sky: #1aa2ec;
    --sky-ray: #37b6f3;
    --sky-glow: #8fdafc;
    --white: #ffffff;
    --sun-yellow: #f4f21f;
    --magenta: #c41fd4;
    --ink: #1c1c1c;
    --city-light: #eef1f8;
    --city-mid: #b7bfdc;
    --city-deep: #5e6a8c;
    --gold-light: #e2b84a;
    --gold-deep: #9a6a1c;
    --jade: #3f9a78;
    --jade-deep: #2c6b55;
  }
  html, body {
    margin: 0;
    padding: 0;
    width: 1200px;
    height: 1200px;
    overflow: hidden;
  }
  .cover {
    position: relative;
    width: 1200px;
    height: 1200px;
    overflow: hidden;
    font-family: 'Montserrat', sans-serif;
    background:
      radial-gradient(circle at 604px 436px, var(--sky-glow) 0, rgba(143,218,252,0) 440px),
      repeating-conic-gradient(from 0deg at 604px 436px, var(--sky) 0deg 7.5deg, var(--sky-ray) 7.5deg 15deg);
  }
  .emblem {
    position: absolute;
    left: 0;
    top: 0;
    width: 1200px;
    height: 1200px;
  }
  .arc-title {
    font-family: 'Montserrat', sans-serif;
    font-weight: 800;
    font-size: 100px;
    fill: var(--white);
  }
  .arc-word {
    font-family: 'Montserrat', sans-serif;
    font-weight: 900;
    font-size: 145px;
    fill: var(--sun-yellow);
  }
  .arc-word-shadow {
    fill: var(--magenta);
  }
  .details {
    position: absolute;
    left: 0;
    top: 890px;
    width: 1200px;
    display: flex;
    flex-direction: column;
    align-items: center;
  }
  .venue {
    background: var(--sun-yellow);
    color: var(--ink);
    font-weight: 500;
    font-size: 44px;
    line-height: 74px;
    height: 74px;
    padding: 0 20px;
  }
  .dates {
    margin-top: 14px;
    color: var(--sun-yellow);
    font-weight: 800;
    font-size: 58px;
    line-height: 68px;
    letter-spacing: -1px;
    text-shadow: -3px 3px 0 var(--magenta);
  }
  .hashtag {
    margin-top: 4px;
    color: var(--white);
    font-weight: 400;
    font-size: 46px;
    line-height: 56px;
  }
</style>
</head>
<body>
<main class="cover">
  <svg class="emblem" viewBox="0 0 1200 1200" width="1200" height="1200">
    <defs>
      <linearGradient id="cityTone" x1="0" y1="0" x2="0.3" y2="1">
        <stop offset="0" stop-color="var(--city-light)"/>
        <stop offset="0.55" stop-color="var(--city-mid)"/>
        <stop offset="1" stop-color="var(--city-deep)"/>
      </linearGradient>
      <linearGradient id="dragonTone" x1="0" y1="0" x2="1" y2="0.4">
        <stop offset="0" stop-color="var(--gold-deep)"/>
        <stop offset="0.35" stop-color="var(--gold-light)"/>
        <stop offset="0.6" stop-color="var(--jade)"/>
        <stop offset="1" stop-color="var(--jade-deep)"/>
      </linearGradient>
      <clipPath id="badgeClip">
        <circle cx="604" cy="436" r="228"/>
      </clipPath>
      <path id="topArc" d="M 330 520 A 280 280 0 1 1 878 520"/>
      <path id="bottomArc" d="M 232 436 A 372 372 0 0 0 976 436"/>
    </defs>

    <circle class="badge-ring" cx="604" cy="436" r="242" fill="var(--white)"/>
    <circle class="city-photo" cx="604" cy="436" r="228" fill="url(#cityTone)"
            role="img" aria-label="Photo of the twin curved city hall towers under a bright sky"/>

    <rect class="dragon-photo" x="440" y="500" width="490" height="170" rx="85"
          transform="rotate(-10 685 585)" fill="url(#dragonTone)"
          role="img" aria-label="Photo of a golden dragon sculpture with a green mane, reaching out of the circle"/>

    <text class="arc-title">
      <textPath href="#topArc" startOffset="50%" text-anchor="middle" textLength="1000" lengthAdjust="spacing">TORONTO LANTERN</textPath>
    </text>

    <g transform="translate(-5,5)">
      <text class="arc-word arc-word-shadow">
        <textPath href="#bottomArc" startOffset="50%" text-anchor="middle" letter-spacing="12">FAIR</textPath>
      </text>
    </g>
    <text class="arc-word">
      <textPath href="#bottomArc" startOffset="50%" text-anchor="middle" letter-spacing="12">FAIR</textPath>
    </text>
  </svg>

  <section class="details">
    <div class="venue">Corwin Ashby Square</div>
    <div class="dates">July 15 &amp; 16</div>
    <div class="hashtag">#LanternFairTo</div>
  </section>
</main>
</body>
</html>
```